Hair salon and Nail salon in Hawaii need a newspaper Ad design.

We need a newspaper Ad design for new open hair & nail salon in Waikiki Hawaii.Our Recommendation service for hair is "Head Spa" $30+tax and for nail is "Manicure Treatment Course" (Filing+Cuticle Care+Massage+Coloring) $20+tax.
We would like to see Hawaiian taste color and also having sense of luxury design. The ad size is W 5.0” x H 6.375”.
I would customers to know the shop place(Lanakila Crest Hotel 1F) , phone(808-555-0173), instagram(salonbrightwave) , our web site https://salonbrightwave.example and recommend services. For Web or Instagram , QR code is acceptable.

Target Market(s)

women & men

Industry/Entity Type

Beauty Salon

Font styles to use
Serif

Colors

Designer to choose colors to be used in the design.

Requirements
Must have
• Tagline for local customers. Shop Name is "SALON BRIGHTWAVE".the shop place(Lanakila Crest Hotel 1F) , phone(808-555-0173), instagram(salonbrightwave) and recommend services.
Nice to have
• Our services are competitive, but we don't want to be seen as just cheap and low quality.

```html
<!DOCTYPE html>
<html lang="en">
<head>
<meta charset="utf-8">
<title>Salon Brightwave — Newspaper Ad</title>
<link rel="stylesheet" href="https://fonts.googleapis.com/css2?family=Poppins:wght@300;400;500;600;700&display=swap">
<style>
  :root {
    --page: #d9d9d9;
    --peach: #f1d7b3;
    --teal: #1d3a47;
    --orange: #e8601c;
    --yellow: #e4aa17;
    --coral: #ec5f4e;
    --ink: #1f3440;
    --white: #ffffff;
  }
  * { box-sizing: border-box; margin: 0; padding: 0; }
  html, body { width: 1200px; height: 900px; overflow: hidden; background: var(--page); }
  body { font-family: "Poppins", sans-serif; color: var(--ink); }

  .ad {
    position: absolute; left: 50px; top: 74px;
    width: 1100px; height: 752px; overflow: hidden;
    background: var(--peach);
  }
  .ad__shapes { position: absolute; inset: 0; }

  .brand { position: absolute; left: 690px; top: 78px; width: 210px; display: flex; flex-direction: column; align-items: center; gap: 8px; }
  .brand__mark { width: 40px; height: 40px; background: var(--white); }
  .brand__name { font-weight: 300; font-size: 23px; color: var(--ink); letter-spacing: 0.5px; white-space: nowrap; }

  .headline { position: absolute; right: 200px; top: 170px; text-align: right; line-height: 1.45; }
  .headline__lead { font-size: 31px; font-weight: 400; color: var(--ink); letter-spacing: 0.5px; }
  .headline__main { font-size: 33px; font-weight: 500; color: var(--orange); letter-spacing: 0.5px; }
  .headline__main strong { font-weight: 700; }

  .intro { position: absolute; right: 175px; top: 366px; text-align: right; font-size: 18px; line-height: 1.3; color: var(--ink); }

  .service-pill {
    position: absolute; left: 640px; top: 432px; width: 270px; height: 40px;
    border-radius: 20px; background: var(--coral); color: var(--white);
    font-size: 17px; font-weight: 600; display: flex; align-items: center; justify-content: center;
  }

  .price-list { position: absolute; left: 560px; top: 496px; width: 370px; font-size: 16px; color: var(--ink); }
  .price-row { position: relative; border-bottom: 2px dotted var(--ink); padding-bottom: 2px; margin-bottom: 16px; }
  .price-row__name { display: block; white-space: nowrap; line-height: 1.5; }
  .price-row__price { position: absolute; right: 0; top: 0; font-weight: 500; white-space: nowrap; line-height: 1.5; }
  .price-row--first { padding-top: 24px; }

  .contact { position: absolute; left: 60px; top: 606px; font-size: 16px; font-weight: 600; color: var(--ink); font-style: normal; }
  .contact__item { display: flex; align-items: center; gap: 10px; height: 27px; white-space: nowrap; }
  .contact__item svg { width: 16px; height: 16px; fill: var(--ink); flex: none; }
</style>
</head>
<body>
<main class="ad">
  <svg class="ad__shapes" viewBox="0 0 1100 752">
    <defs>
      <linearGradient id="portrait-tone" x1="0" y1="0" x2="1" y2="1">
        <stop offset="0" stop-color="#a9714a"/>
        <stop offset="0.5" stop-color="#c8946a"/>
        <stop offset="1" stop-color="#e9cba6"/>
      </linearGradient>
      <linearGradient id="peach-tone" x1="0" y1="0" x2="1" y2="0">
        <stop offset="0" stop-color="#e9c9a0"/>
        <stop offset="1" stop-color="#f4dcbc"/>
      </linearGradient>
      <radialGradient id="hand-tone">
        <stop offset="0" stop-color="#e8c4a8"/>
        <stop offset="1" stop-color="#c89472"/>
      </radialGradient>
      <linearGradient id="flora-tone" x1="0" y1="0" x2="1" y2="1">
        <stop offset="0" stop-color="#f2a13a"/>
        <stop offset="0.5" stop-color="#ec6a5a"/>
        <stop offset="1" stop-color="#5e9a4a"/>
      </linearGradient>
    </defs>

    <rect class="bg-peach" width="1100" height="752" fill="url(#peach-tone)"/>
    <rect class="portrait" x="20" y="0" width="540" height="560" fill="url(#portrait-tone)" role="img" aria-label="Portrait of a smiling woman with voluminous curly hair"/>

    <polyline class="frame-top" points="55,200 55,46 920,46 920,250" stroke="var(--teal)" stroke-width="2" fill="none"/>

    <path class="band-yellow" d="M0,500 C320,500 440,292 1100,282 L1100,752 L0,752 Z" fill="var(--yellow)"/>
    <path class="panel-white" d="M462,752 L462,570 C520,420 640,330 1100,318 L1100,752 Z" fill="var(--white)" stroke="var(--orange)" stroke-width="4"/>
    <path class="band-orange" d="M0,486 C320,486 440,270 1100,258 L1100,282 C440,292 320,512 0,512 Z" fill="var(--orange)"/>
    <path class="band-teal" d="M0,440 C320,440 440,240 1100,230 L1100,262 C440,272 320,500 0,528 Z" fill="var(--teal)"/>

    <polyline class="frame-bottom" points="942,330 942,640 600,640" stroke="var(--yellow)" stroke-width="2.5" fill="none"/>
    <line class="panel-rule" x1="462" y1="735" x2="1100" y2="735" stroke="var(--orange)" stroke-width="4"/>

    <circle class="nail-photo-ring" cx="433" cy="463" r="96" fill="var(--teal)"/>
    <circle class="nail-photo" cx="433" cy="463" r="86" fill="url(#hand-tone)" stroke="var(--white)" stroke-width="4" role="img" aria-label="Close-up of manicured hand holding a tropical flower"/>

    <rect class="flora" x="955" y="400" width="145" height="230" rx="60" fill="url(#flora-tone)" opacity="0.85" role="img" aria-label="Watercolour hibiscus flowers and tropical leaves"/>
    <rect class="flora" x="880" y="648" width="190" height="80" rx="36" fill="url(#flora-tone)" opacity="0.7" role="img" aria-label="Tropical leaves"/>
  </svg>

  <div class="brand">
    <span class="brand__mark"></span>
    <span class="brand__name">salonbrightwave</span>
  </div>

  <h1 class="headline">
    <span class="headline__lead">Are you ready for a</span><br>
    <span class="headline__main">NEW &amp; BETTER <strong>YOU?</strong></span>
  </h1>

  <p class="intro">Our newly opened Hair and Nail salon<br>now in Waikiki, Hawaii</p>

  <div class="service-pill">Our Recommended Service</div>

  <div class="price-list">
    <div class="price-row price-row--first">
      <span class="price-row__name">Head Spa</span>
      <span class="price-row__price">$30+tax</span>
    </div>
    <div class="price-row">
      <span class="price-row__name">Manicure Treatment Course</span>
      <span class="price-row__name">(Filing+Cuticle Care+Massage+Coloring)</span>
      <span class="price-row__price">$20+tax</span>
    </div>
  </div>

  <address class="contact">
    <div class="contact__item">
      <svg viewBox="0 0 16 16"><path d="M8 0a5.5 5.5 0 0 0-5.5 5.5C2.5 10 8 16 8 16s5.5-6 5.5-10.5A5.5 5.5 0 0 0 8 0zm0 8a2.5 2.5 0 1 1 0-5 2.5 2.5 0 0 1 0 5z"/></svg>
      Lanakila Crest Hotel 1F
    </div>
    <div class="contact__item">
      <svg viewBox="0 0 16 16"><path d="M3.6 1l2.3 2.6-1.3 2c.9 1.9 2.3 3.3 4.2 4.2l2-1.3L15 11l-1.4 3.2C7.4 14.6 1.4 8.6 1.8 2.4z"/></svg>
      808-555-0173
    </div>
    <div class="contact__item">
      <svg viewBox="0 0 16 16"><circle cx="8" cy="8" r="6.5" fill="none" stroke="#1f3440" stroke-width="1.6"/><path d="M1.5 8h13M8 1.5c2.2 2 2.2 11 0 13M8 1.5c-2.2 2-2.2 11 0 13" fill="none" stroke="#1f3440" stroke-width="1.2"/></svg>
      www.salonbrightwave.example
    </div>
    <div class="contact__item">
      <svg viewBox="0 0 16 16"><circle cx="8" cy="8" r="6" fill="none" stroke="#1f3440" stroke-width="1.8"/></svg>
      salonbrightwave
    </div>
  </address>
</main>
</body>
</html>
```